Dental Learning Allies Needs a Great Looking Sales Brochure!

Please help us design a brochure for our company, Dental Learning Allies, LLC to use for sales and prospecting!
It is our first brochure, and as we are a small company, we don't normally use them, but we have an upcoming meeting and need a GREAT looking brochure with a call to action!
In addition to a pdf print ready version of the file, we need to receive a version with editable pdf text fields.
Our original thought is a 1-page, 4-panel fold or Tri-fold brochure, but we are open to recommendations based on the content.
More about us: We are a small company specializing in education, motivational speaking and event services for dental practices both large and big dental groups. You can check out our website at https://dentallearningallies.example
I have uploaded our logo files, some images for consideration, and proposed text content for the brochure. Note - if you have the space to add our KRV MOTO provider approval we would like to. If you do use the KRV Moto logo, we need to follow their logo guidelines which are also attached.
Should you have any questions, please don't hesitate to ask!
Thank you for helping make us look great!!!!

Target Market(s)

Dental Support Organizations (DSO's)

Font styles to use
Serif
Sans Serif

Requirements
Must have
• Our company logo
• At least 1-2 photos
• Professional look and feel
• Text from uploaded word document for proposed copy
Nice to have
• KRV logo and language showing we are KRV MOTO provider

```html
<!DOCTYPE html>
<html lang="en">
<head>
<meta charset="utf-8">
<title>Dental Learning Allies – Flyer</title>
<link rel="stylesheet" href="https://fonts.googleapis.com/css2?family=Cinzel:wght@600;700&family=PT+Sans:wght@400;700&display=swap">
<style>
  :root{
    --green:#1e9640;
    --blue:#1467b7;
    --navy:#0f5aa5;
    --ink:#2b2b2b;
    --page:#e9e9e9;
    --white:#ffffff;
  }
  *{box-sizing:border-box;margin:0;padding:0}
  html,body{width:1200px;height:1200px;overflow:hidden;background:var(--page)}
  body{position:relative;font-family:"PT Sans",sans-serif;color:var(--ink)}
  .flyer{position:absolute;left:202px;top:43px;width:795px;height:1114px;background:var(--white);overflow:hidden;box-shadow:0 2px 10px rgba(0,0,0,.15)}
  .flyer > *{position:absolute}
  .hero-bg{left:0;top:0;width:795px;height:600px;background:linear-gradient(180deg,rgba(255,255,255,0) 70%,#ffffff 100%),linear-gradient(100deg,#ffffff 0%,#eef3f6 45%,#dfe7ec 75%,#eaf0f3 100%)}
  .portrait{left:430px;top:44px;width:365px;height:480px;background:radial-gradient(ellipse at 55% 35%,#e4d3bd 0%,#c9b9a3 28%,#8d8a83 55%,#6f6e6a 80%,rgba(111,110,106,0) 100%);border-radius:48% 48% 0 0}
  .brand{left:43px;top:64px;display:flex;align-items:center;gap:16px}
  .brand-mark{width:44px;height:44px;background:var(--green)}
  .brand-name{font-family:"Cinzel",serif;font-weight:600;color:var(--blue);font-size:30px;line-height:36px}
  .rule{height:4px;background:var(--blue)}
  .hero-rule{left:24px;top:176px;width:74px}
  .headline{left:24px;top:188px;font-family:"Cinzel",serif;font-weight:700;line-height:1}
  .headline .lead{display:block;color:var(--green);font-size:48px;margin-bottom:6px}
  .headline .sub{display:block;color:var(--navy);font-size:35px;line-height:42px}
  .call-band{left:0;top:346px;width:448px;height:37px;background:var(--green);border-radius:0 19px 19px 0;display:flex;align-items:center;padding-left:30px;gap:6px;color:var(--white);font-family:"Cinzel",serif;font-weight:600;font-size:24px}
  .call-band svg{width:20px;height:20px}
  .wave{left:0;top:0;width:795px;height:700px}
  .section-title{font-family:"Cinzel",serif;font-weight:700;color:var(--green)}
  .services-title{left:91px;top:512px;font-size:31px;line-height:36px}
  .services-rule{left:91px;top:550px;width:77px}
  .service{display:flex;align-items:center;gap:18px;font-size:15px;line-height:18px;color:var(--ink)}
  .service-icon{width:60px;height:60px;border-radius:50%;background:var(--green);display:flex;align-items:center;justify-content:center;flex:none}
  .service-icon svg{width:36px;height:36px;fill:none;stroke:var(--white);stroke-width:2;stroke-linecap:round;stroke-linejoin:round}
  .why-title{left:24px;top:706px;font-size:32px}
  .why-lead{left:30px;top:746px;font-size:17px;line-height:22px;font-weight:700;color:var(--blue)}
  .why-rule{left:30px;top:771px;width:74px}
  .why-list{list-style:none;font-size:14.5px;line-height:18.5px}
  .why-list li{position:relative;padding-left:12px}
  .why-list li::before{content:"•";position:absolute;left:0;font-size:11px}
  .list-left{left:30px;top:783px;width:350px}
  .list-left li{margin-bottom:11px}
  .list-right{left:418px;top:782px;width:340px}
  .list-right li{margin-bottom:11px}
  .yes-pill{left:118px;top:926px;width:538px;height:30px;border-radius:15px;background:var(--blue);color:var(--white);font-weight:700;font-size:16.5px;display:flex;align-items:center;justify-content:center}
  .testimonial{left:0;top:973px;width:795px;height:103px;background:var(--green);color:var(--white);padding:14px 40px 0 40px;font-size:14.4px;line-height:18.4px}
  .testimonial cite{display:block;font-style:normal;text-align:right;margin-top:5px;padding-right:8px}
  .footer{left:0;top:1076px;width:795px;height:38px;background:var(--blue);color:var(--white);display:flex;align-items:center;justify-content:center;font-size:16px;letter-spacing:3px}
</style>
</head>
<body>
<main class="flyer">
  <div class="hero-bg" role="img" aria-label="Softly blurred bright office hallway"></div>
  <div class="portrait" role="img" aria-label="Photo of a smiling professional woman in a grey blazer with arms crossed"></div>

  <svg class="wave" viewBox="0 0 795 700" aria-hidden="true">
    <path d="M0 480 C60 420 150 395 230 410 C330 430 420 500 575 510 C480 535 380 480 280 474 C130 465 40 500 0 600 Z" fill="#1467b7"/>
    <path d="M430 481 C520 470 640 470 795 520 L795 636 C760 575 700 525 610 505 C560 496 480 492 430 481 Z" fill="#1467b7"/>
  </svg>

  <div class="brand">
    <span class="brand-mark"></span>
    <span class="brand-name">Dental<br>Learning Allies</span>
  </div>

  <div class="rule hero-rule"></div>
  <h1 class="headline">
    <span class="lead">Grow Your</span>
    <span class="sub">DSO with Customized</span>
    <span class="sub">Training Solutions</span>
  </h1>

  <div class="call-band">
    <span>Call Us Today !</span>
    <svg viewBox="0 0 24 24" aria-hidden="true"><circle cx="12" cy="12" r="10" fill="none" stroke="#fff" stroke-width="1.8"/><path d="M8.5 7.5c.5-.5 1.2-.4 1.5.2l.8 1.6c.2.4.1.9-.2 1.2l-.6.6c.6 1.2 1.6 2.2 2.8 2.8l.6-.6c.3-.3.8-.4 1.2-.2l1.6.8c.6.3.7 1 .2 1.5l-.8.8c-.6.6-1.6.8-2.4.4-2.5-1.2-4.4-3.1-5.6-5.6-.4-.8-.2-1.8.4-2.4z" fill="#fff"/></svg>
    <span>(555) 013-4620</span>
  </div>

  <h2 class="section-title services-title">Services</h2>
  <div class="rule services-rule"></div>

  <div class="service" style="left:38px;top:556px">
    <span class="service-icon"><svg viewBox="0 0 36 36"><rect x="9" y="5" width="20" height="14"/><circle cx="6" cy="10" r="2.5"/><path d="M6 13v8M6 15l6-2"/><circle cx="12" cy="26" r="2.5"/><circle cx="20" cy="26" r="2.5"/><circle cx="28" cy="26" r="2.5"/><path d="M8 33c0-3 8-3 8 0M16 33c0-3 8-3 8 0M24 33c0-3 8-3 8 0"/></svg></span>
    <span>Clinical Training</span>
  </div>
  <div class="service" style="left:276px;top:556px">
    <span class="service-icon"><svg viewBox="0 0 36 36"><path d="M10 16a6 6 0 0 1 2-11 8 8 0 0 1 14 3 5 5 0 0 1 0 10"/><rect x="8" y="17" width="20" height="12" rx="1"/><path d="M12 21h6M12 25h10M14 29v3M22 29v3"/></svg></span>
    <span>Web-Based Learning</span>
  </div>
  <div class="service" style="left:530px;top:556px">
    <span class="service-icon"><svg viewBox="0 0 36 36"><circle cx="10" cy="9" r="3"/><path d="M6 26v-8a4 4 0 0 1 8 0v8M20 22h12M22 22v10M30 22v10M24 22v-8h6v8"/><circle cx="17" cy="15" r="2.5"/></svg></span>
    <span>Chairside Coaching</span>
  </div>
  <div class="service" style="left:38px;top:631px">
    <span class="service-icon"><svg viewBox="0 0 36 36"><circle cx="18" cy="18" r="14"/><path d="M6 15h24M14 15v-5a2 2 0 0 1 4 0v5M18 11a2 2 0 0 1 4 0v4M14 15v8l2 3v6M22 15v8l-2 3v6"/></svg></span>
    <span>Train Your Trainer</span>
  </div>
  <div class="service" style="left:276px;top:631px">
    <span class="service-icon"><svg viewBox="0 0 36 36"><rect x="5" y="5" width="18" height="9" rx="4"/><path d="M10 9.5h0M14 9.5h0M18 9.5h0"/><circle cx="12" cy="21" r="3"/><circle cx="25" cy="21" r="3"/><path d="M5 31c0-4 14-4 14 0M18 31c0-4 14-4 14 0"/></svg></span>
    <span>Regional or<br>Annual Meetings</span>
  </div>
  <div class="service" style="left:530px;top:631px">
    <span class="service-icon"><svg viewBox="0 0 36 36"><path d="M5 31h26M8 31v-8h4v8M14 31v-11h4v11M20 31v-14h4v14M26 31v-20h4v20M7 18l8-5 5 2 9-8"/></svg></span>
    <span>Metric Analytics</span>
  </div>

  <h2 class="section-title why-title">Why partner with us?</h2>
  <p class="why-lead">Do you want to :</p>
  <div class="rule why-rule"></div>

  <ul class="why-list list-left">
    <li>Make hygiene the driver of every dental practice?</li>
    <li>Consistently achieve production goals?</li>
    <li>Provide excellent care for every patient in every practice?</li>
    <li>Provide continuity of care between providers?</li>
  </ul>
  <ul class="why-list list-right">
    <li>Standardize scripting to increase treatment enrollment?</li>
    <li>Improve the retention of both your staff and your patients?</li>
    <li>Supplement your education initiatives with metrics-based needs assessment?</li>
  </ul>

  <p class="yes-pill">If you said yes to any of these questions, then DLA is right for you!</p>

  <blockquote class="testimonial">
    “Dental Learning Allies delivered training for our team that isn't offered anywhere else. Their training has dramatically changed our team’s ability to influence treatment acceptance. I would recommend their services to any DSO looking to increase profitability !”
    <cite>-&nbsp;&nbsp;&nbsp;&nbsp;&nbsp;Dr. Martin Hale, Chief Clinical Officer, Harbor Smile Practice Group</cite>
  </blockquote>

  <footer class="footer">dentallearningallies.example</footer>
</main>
</body>
</html>
```